Business Card for Ferncliff Massage

I need a business card for my massage therapy & cannabis oil practice. I already have a logo,the "massage" got edited out of this file. I will send the original soon. I need these elements to be on the card:
web: FerncliffMassage.example
ph: 541/382-9147
email: Marla.Quintavelle@mailbox.example
Other slogans, statements to consider:
Science Geek, Massage Therapist, Neuromuscular Therapy, Cannabis Spa Treatments, Raindrop Therapy, Essential Oils
Target Market(s)
women between 20 & 65, people with enough $ to afford regular massage, people who recently had a motor vehicle accident, Halvora HMC insured
Industry/Entity Type
Massage Therapy
Contact Information for Business Card
I would like to see my bear logo featured; contact details, greens & blues preferred colors.

```html
<!DOCTYPE html>
<html lang="en">
<head>
<meta charset="utf-8">
<title>Ferncliff Massage – Business Card</title>
<link rel="stylesheet" href="https://fonts.googleapis.com/css2?family=Open+Sans:wght@400;600;700&family=PT+Sans+Narrow:wght@400&display=swap">
<style>
  :root {
    --backdrop: #000000;
    --card-light: #f3f3f3;
    --card-blue: #0b93d0;
    --brand-teal: #1ba99a;
    --brand-blue: #1b8fd0;
    --ink: #222222;
    --white: #ffffff;
    --bullet: #dff1fa;
  }
  * { margin: 0; padding: 0; box-sizing: border-box; }
  html, body {
    width: 1200px; height: 900px; overflow: hidden;
    background: var(--backdrop);
    font-family: "Open Sans", Arial, sans-serif;
  }
  .canvas { position: relative; width: 1200px; height: 900px; }

  .card { position: absolute; top: 200px; width: 310px; height: 502px; }
  .card-front {
    left: 265px; background: var(--card-light);
    border-radius: 72px 0 72px 0;
  }
  .card-back {
    left: 641px; background: var(--card-blue);
    border-radius: 0 72px 0 72px;
  }

  .brand-mark {
    position: absolute; left: 110px; top: 60px;
    width: 90px; height: 90px; border-radius: 50%;
    background: var(--brand-blue);
  }
  .brand-name {
    position: absolute; left: 0; right: 0; top: 178px;
    text-align: center;
    font-family: "PT Sans Narrow", "Arial Narrow", sans-serif;
    font-size: 40px; line-height: 1; color: var(--brand-teal);
  }

  .contact { position: absolute; left: 22px; top: 323px; }
  .person-name { font-size: 19px; font-weight: 600; color: var(--brand-blue); line-height: 1.2; }
  .person-role { font-size: 14px; color: var(--ink); margin-top: 2px; }
  .contact-list { list-style: none; margin-top: 10px; }
  .contact-item {
    display: flex; align-items: center; gap: 8px;
    font-size: 13.5px; color: var(--ink); line-height: 20px;
  }
  .contact-item svg { width: 12px; height: 12px; fill: var(--brand-blue); flex: none; }
  .website { font-size: 13.5px; color: var(--brand-blue); margin-top: 5px; }

  .services {
    position: absolute; left: 40px; top: 177px; list-style: none;
  }
  .service {
    display: flex; align-items: center; gap: 5px;
    font-size: 15.5px; font-weight: 600; color: var(--white);
    text-transform: uppercase; height: 30px;
  }
  .service::before {
    content: ""; width: 16px; height: 9px; border-radius: 50% 60% 45% 55%;
    background: var(--bullet); flex: none;
  }
</style>
</head>
<body>
<main class="canvas">
  <section class="card card-front">
    <span class="brand-mark" aria-hidden="true"></span>
    <p class="brand-name">Ferncliff Massage</p>

    <div class="contact">
      <p class="person-name">Dana Whitlock</p>
      <p class="person-role">President</p>
      <ul class="contact-list">
        <li class="contact-item">
          <svg viewBox="0 0 24 24" aria-hidden="true"><path d="M6.6 10.8a15.1 15.1 0 0 0 6.6 6.6l2.2-2.2a1 1 0 0 1 1-.25 11.4 11.4 0 0 0 3.6.57 1 1 0 0 1 1 1V20a1 1 0 0 1-1 1A17 17 0 0 1 3 4a1 1 0 0 1 1-1h3.5a1 1 0 0 1 1 1c0 1.25.2 2.46.57 3.6a1 1 0 0 1-.25 1z"/></svg>
          541/382-9147
        </li>
        <li class="contact-item">
          <svg viewBox="0 0 24 24" aria-hidden="true"><path d="M2 5h20v14H2z" opacity=".0"/><path d="M2 6l10 6 10-6V5H2zm0 2.3V19h20V8.3l-10 6z"/></svg>
          Marla.Quintavelle@mailbox.example
        </li>
      </ul>
      <p class="website">FerncliffMassage.example</p>
    </div>
  </section>

  <section class="card card-back">
    <ul class="services">
      <li class="service">Science Geek</li>
      <li class="service">Massage Therapist</li>
      <li class="service">Neuromuscular Therapy</li>
      <li class="service">Cannabis Spa Treatments</li>
      <li class="service">Raindrop Therapy</li>
      <li class="service">Essential Oils</li>
    </ul>
  </section>
</main>
</body>
</html>
```